UNABLE TO FIND SUITABLE ICT TALENT IN NEW ZEALAND? WE CAN HELP.

We need a brochure to sell our migration services to ICT (Information and Communication Technologies) recruiters in New Zealand. We are a New Zealand based migration company headed by a Licensed Immigration Adviser and we can bring in specific talents into New Zealand. We are aware ICT is in the long term skill shortage area and that recruiters and companies are struggling to find the right ICT talent. So over the past two years we have developed a high quality global ICT talent pool who are keen to work in New Zealand. And we have the expertise to and process their legal entry into New Zealand bring them in at short notice. We need a brochure that conveys a strong New Zealand connect, confidence and trust.

Target Market(s)

New Zealand ICT Recruiters and Companies who need ICT talent

Industry/Entity Type

Communication

Contact Information for Business Card

Marlow Feltis
Senior Manager - Operations
Mobile: 0213394625

Font styles to use
Serif

Requirements
Must have
• A strong ICT and New Zealand theme. Must have the following Maori proverb on the rear with the English translation. The rear side of the card which has this proverb must also have a strong Maori theme.
• Naku te rourou nau te rourou ka ora ai te iwi - With your basket and my basket the people will live
Nice to have
• The brochure/flyer is intended to be an A4 size folded in half, so that we can print and mail it to our target clients. Remember this is an A4 flyer folded in the middle. So it has got cover + back + 2 inside pages in all.

```html
<!DOCTYPE html>
<html lang="en">
<head>
<meta charset="utf-8">
<title>ICT Talent Brochure – Inside Spread</title>
<link rel="stylesheet" href="https://fonts.googleapis.com/css2?family=Barlow:wght@300;400&family=Barlow+Semi+Condensed:wght@500;600&display=swap">
<style>
  :root {
    --purple: #4a1a72;
    --purple-deep: #3b1460;
    --heading: #3d1a6e;
    --body: #3a3a3a;
    --paper: #ffffff;
    --night: #070708;
    --cost-text: #c9c9cc;
  }
  * { margin: 0; padding: 0; box-sizing: border-box; }
  html, body { width: 1200px; height: 855px; overflow: hidden; background: var(--paper); }
  .spread { position: relative; width: 1200px; height: 855px; background: var(--paper); overflow: hidden; font-family: "Barlow", Arial, sans-serif; }
  .top-band { position: absolute; left: 0; top: 0; width: 1200px; height: 30px; background: var(--purple); }
  .hero-visual { position: absolute; left: 0; top: 30px; width: 612px; height: 186px;
    background: radial-gradient(ellipse at 35% 45%, #2aa6e0 0%, #136aa6 40%, #0a2c55 75%, #05080f 100%); }
  .cost-panel { position: absolute; left: 612px; top: 30px; width: 588px; height: 186px; background: var(--night); padding: 38px 36px 0 25px; }
  .cost-panel h2 { font-family: "Barlow Semi Condensed", Arial, sans-serif; font-weight: 500; font-size: 14.5px; color: #fff; letter-spacing: 0.3px; margin-bottom: 15px; line-height: 18px; }
  .cost-panel p { font-weight: 300; font-size: 13.4px; line-height: 16.8px; color: var(--cost-text); letter-spacing: 0.2px; }
  .fold-shadow { position: absolute; left: 600px; top: 216px; width: 70px; height: 588px;
    background: linear-gradient(90deg, rgba(0,0,0,0.28) 0%, rgba(0,0,0,0.08) 45%, rgba(0,0,0,0) 100%); }
  .column { position: absolute; top: 244px; width: 238px; color: var(--body); }
  .column h3 { font-family: "Barlow Semi Condensed", Arial, sans-serif; font-weight: 500; font-size: 14.5px; color: var(--heading); letter-spacing: 0.3px; margin-bottom: 16px; line-height: 17px; }
  .column p { font-weight: 300; font-size: 13.2px; line-height: 16.8px; letter-spacing: 0.25px; margin-bottom: 16.8px; }
  .col-1 { left: 49px; }
  .col-2 { left: 328px; }
  .col-3 { left: 638px; }
  .col-4 { left: 917px; width: 242px; }
  .footer-pattern { position: absolute; left: 0; top: 804px; width: 1200px; height: 51px;
    background: linear-gradient(180deg, var(--purple-deep) 0%, #6a3f94 50%, var(--purple-deep) 100%); }
</style>
</head>
<body>
<main class="spread">
  <div class="top-band"></div>
  <div class="hero-visual" role="img" aria-label="Businessman's open hand beneath a glowing blue network of connected people icons"></div>

  <section class="cost-panel">
    <h2>WHAT WILL IT COST US?</h2>
    <p>We offer a fixed cost to you at $2000+GST for each successful placement. You pay us only when you get paid from your end client. There is no hidden cost whatsoever. We are able to offer this fixed, low cost to you because we charge the client a processing fee for the visa and also for creating this opportunity for them in New Zealand.</p>
  </section>

  <div class="fold-shadow"></div>

  <section class="column col-1">
    <h3>WHAT IS THE SERVICE YOU PROVIDE?</h3>
    <p>Put simply, if you are unable to find a particular ICT talent in New Zealand, we can find such specific personnel from our vast global database of ICT professionals and bring them into New Zealand on a valid work visa within weeks.</p>
    <h3>HOW DOES THIS WORK?</h3>
    <p>We are a migration company headed by a Licensed Immigration Adviser and we can bring in specific talents into New Zealand. We are aware ICT is in the long term skill shortage area and that recruiters and companies are struggling to find the right ICT talent. So over the past two years we have developed a high quality global ICT talent pool who are keen to work in New Zealand. And we have the expertise to and process their legal entry into New Zealand bring them in at short notice.</p>
    <h3>HOW GOOD IS YOUR TALENT POOL?</h3>
    <p>You name it and we got it. Our talent pool has top notch, impeccable English</p>
  </section>

  <section class="column col-2">
    <p>speaking ICT professionals currently working with the who's who of the ICT industry globally. And we are talking senior level professionals in Glimmerweb, Microvane, Dellmont, Norvale and such. They are in Singapore, India, UK, USA and practically everywhere. We have already sold them the idea of New Zealand as a destination and they are eager to look for a break to come and enjoy being in Aotearoa. Mostly for the lifestyle it offers them and their family.</p>
    <h3>WHAT IS THE PROCESS?</h3>
    <p>Simple. Give us your requirements and we will put our team to work and give you handpicked CVs for each available position at a ratio of 1:10. We will then coordinate with you locally here in New Zealand and set up Vidlink and/or telephonic interviews. If you like someone, set them up for an interview with your end client. And if they like them and make a job offer, we will step in and sort out the work visa in no time. We can have them here within 48 weeks and also negotiate with them on a case by case basis.</p>
  </section>

  <section class="column col-3">
    <h3>WHO ARE YOU GUYS?</h3>
    <p>We are veterans of the New Zealand migration industry, recognised by the government and with a pedigree spanning over a decade. We are keen to align with local New Zealand based ICT recruitment firms to address the skill shortage in the industry by sourcing high quality talent from overseas and process their legal entry into New Zealand. We are extremely value driven and will never shortchange our relationship with you. Our desire is to access top IT talent globally, sell the idea of New Zealand as a destination to them and create a legitimate entry pathway for these professionals through a collaboration with you. The vision and mission is to become the recruiter to the New Zealand ICT recruiters.</p>
    <h3>THE TEAM</h3>
    <p>Tamati Hollis is the managing director and a Licensed Immigration Adviser (License No 210577318). A veteran of the migration industry, he is highly acknowledged within the migration industry and was accorded the</p>
  </section>

  <section class="column col-4">
    <p>privilege of a private audience with the Governor General of New Zealand in recognition of his services.</p>
    <p>Dev Kansal is a director and brings with him over two decades of ICT experience. He has worked in leading ICT roles in New Zealand for over a decade now and with his technical background he is responsible for candidate assessment to ensure suitability to the New Zealand ICT work environment.</p>
    <p>Marlow Feltis is the Senior Operations Manager and your primary contact for engagement and delivery of our services. He has vast experience in New Zealand and Asia and has an enviable track record in education and public relations.</p>
    <p>Sanjay Hollis is the manager responsible for creation of a high quality ICT talent pool to be attracted and moved to New Zealand. He ensures that only the cremedelacreme enter the ICT talent pool available for New Zealand.</p>
  </section>

  <div class="footer-pattern" role="img" aria-label="Purple band with white Maori-inspired kowhaiwhai scroll pattern"></div>
</main>
</body>
</html>
```